Logo for Internal Medicine practice

I want a logo for my Internal Medicine practice, I would like it to be with my name on it which is Lucía Barrenechea Ruiz.

I would like the business card to say the following (it is in Spanish since my practice is in Spanish):

Lucía Barrenechea Ruiz
Medicina Interna
Cel. 5583617204
luciabarrenechearuiz@correovela.mx

Logo Text

Lucía Barrenechea

```html
<!DOCTYPE html>
<html lang="es">
<head>
<meta charset="utf-8">
<title>Lucía Barrenechea Ruiz · Tarjeta de presentación</title>
<link rel="stylesheet" href="https://fonts.googleapis.com/css2?family=Raleway:wght@700&family=Roboto:wght@400&display=swap">
<style>
  :root {
    --teal: #15aec2;
    --ink: #4a4a4a;
    --paper: #ffffff;
    --backdrop: #dedede;
  }
  html, body {
    margin: 0;
    padding: 0;
    width: 1173px;
    height: 1200px;
    overflow: hidden;
    background: var(--backdrop);
  }
  .card {
    position: absolute;
    width: 742px;
    height: 411px;
    box-sizing: border-box;
  }
  .card--front {
    left: 205px;
    top: 150px;
    background: var(--paper);
  }
  .card--back {
    left: 205px;
    top: 637px;
    background: var(--teal);
  }
  .wordmark {
    font-family: "Raleway", sans-serif;
    font-weight: 700;
    text-transform: uppercase;
    letter-spacing: 0.04em;
    line-height: 1.1;
    margin: 0;
  }
  .card--front .wordmark {
    position: absolute;
    right: 60px;
    top: 56px;
    font-size: 32px;
    color: var(--teal);
    text-align: center;
  }
  .card--back .wordmark {
    position: absolute;
    left: 0;
    right: 0;
    top: 138px;
    font-size: 50px;
    color: var(--paper);
    text-align: center;
  }
  .accent-bar {
    position: absolute;
    left: 0;
    top: 250px;
    width: 15px;
    height: 97px;
    background: var(--teal);
  }
  .identity {
    position: absolute;
    left: 60px;
    top: 174px;
  }
  .identity__name {
    margin: 0;
    font-family: "Raleway", sans-serif;
    font-weight: 700;
    font-size: 23px;
    line-height: 1;
    color: var(--teal);
    text-transform: uppercase;
  }
  .identity__role {
    margin: 3px 0 0;
    font-family: "Roboto", sans-serif;
    font-size: 21px;
    line-height: 1.1;
    color: var(--ink);
  }
  .contact {
    position: absolute;
    left: 60px;
    top: 248px;
    font-family: "Roboto", sans-serif;
    font-size: 19px;
    color: var(--ink);
    line-height: 25px;
  }
  .contact__address {
    margin: 0 0 5px;
    font-style: normal;
  }
  .contact__line {
    display: flex;
    align-items: center;
    gap: 9px;
    margin: 0;
  }
  .contact__icon {
    width: 18px;
    height: 18px;
    flex: none;
  }
</style>
</head>
<body>
  <section class="card card--front">
    <p class="wordmark">Lucía<br>Barrenechea</p>
    <div class="accent-bar"></div>
    <div class="identity">
      <h1 class="identity__name">Lucía Barrenechea Ruiz</h1>
      <p class="identity__role">Medicina Interna</p>
    </div>
    <div class="contact">
      <address class="contact__address">37 Calle Las Brisas,<br>Valle Alto, JAL 45130</address>
      <p class="contact__line">
        <svg class="contact__icon" viewBox="0 0 20 20" aria-hidden="true">
          <path fill="#15aec2" d="M2 7c0-2 3-3 8-3s8 1 8 3v1.5h-4V7H6v1.5H2z"/>
          <path fill="#15aec2" d="M5 9h10l2 7H3z"/>
          <rect x="7" y="11" width="6" height="3" fill="#fff"/>
        </svg>
        5583617204
      </p>
      <p class="contact__line">
        <svg class="contact__icon" viewBox="0 0 20 20" aria-hidden="true">
          <path fill="#15aec2" d="M1 8l9-6 9 6v10H1z"/>
          <path fill="#fff" d="M4 8h12v4l-6 3-6-3z"/>
          <path fill="none" stroke="#15aec2" stroke-width="1.4" d="M6 10h8M7 12h6"/>
        </svg>
        luciabarrenechearuiz@correovela.mx
      </p>
    </div>
  </section>

  <section class="card card--back">
    <p class="wordmark">Lucía<br>Barrenechea</p>
  </section>
</body>
</html>
```